CREATE A KILLER WEBSITE DESIGN

We are a firearms training company that trains CIVILIANS (no police or military pictures - thank you!) to defend themselves and are looking for a killer design that's clean, easy to navigate and modern! We want the newest trends applied to this sight like a scrollable site so you can scroll down and see all the features. We are okay with tweaking the HTML but need the artistic design to look good. I'll provide a link to our current site along with a sight we really like so you can get an idea!

I'm supplying a PowerPoint Design we are going with from another designer so you can match the style to the new site.

PAGES: (Please use information from our current site. We like the information but just want a more polished look similar to the NWDFA site below but in our colors.)
Home - Long Form Scrolling Site. Top fold will be a video with a play button.
Falconry Institute - Seven Level Training Program Info Page That Will Contain A Video.
Contact Us - This will be a page that DOES NOT CONTAIN AN EMAIL ADDRESS. Just a contact us form
Meet The Trainer: Brendan Osterlow

Our site:
https://www.brightharborguarding.biz

Sights We Like:
https://www.nwdefenderalliance.com
https://quorvel.com
https://brinmoreworkscorp.com
https://www.pelldrivegear.com

Target Market(s)

Men and women ages 21 to 100 years old

Industry/Entity Type

Self Defense

Number of Pages Required

5+ page

Font styles to use
Sans Serif

Colors
f26267

Requirements
Must have
• Clean and engaging. Use of colors that match our logo.
Should not have
• Poor design quality

```html
<!DOCTYPE html>
<html lang="en">
<head>
<meta charset="utf-8">
<title>Falconry Institute — Harbor Guard Carry</title>
<link href="https://fonts.googleapis.com/css2?family=Audiowide&family=Roboto:wght@400;500;700&display=swap" rel="stylesheet">
<style>
:root{
  --red:#e0101f;
  --red-dark:#b80a16;
  --black:#000;
  --ink:#141414;
  --panel:#1b1b1b;
  --card:#202020;
  --white:#fff;
  --muted:#cfcfcf;
  --display:"Audiowide",sans-serif;
  --body:"Roboto",Arial,sans-serif;
}
*{box-sizing:border-box;margin:0;padding:0}
html,body{width:1200px;height:4706px;overflow:hidden}
body{background:var(--ink);color:var(--white);font-family:var(--body);position:relative}
.abs{position:absolute}
.center{text-align:center}
.display{font-family:var(--display);text-transform:uppercase;letter-spacing:2px}
.red{color:var(--red)}

/* header */
.topbar{position:absolute;left:0;top:0;width:1200px;height:128px;background:var(--black)}
.navbar{position:absolute;left:0;top:128px;width:1200px;height:66px;background:var(--red)}
.btn-outline{position:absolute;top:37px;height:54px;border:2px solid var(--red);border-radius:27px;color:#fff;font-size:12px;font-weight:500;display:flex;align-items:center;justify-content:center;text-transform:uppercase}
.main-nav{position:absolute;top:152px;left:387px;width:702px;display:flex;justify-content:space-between;font-size:12.5px;font-weight:500;text-transform:uppercase}
.brand-shield{position:absolute;left:113px;top:0;width:216px;height:219px}
.brand-name{position:absolute;left:113px;width:216px;text-align:center;font-family:var(--display);color:#fff;font-size:19px;line-height:1.15;text-transform:uppercase}

/* hero */
.hero{position:absolute;top:194px;left:0;width:1200px;height:650px;background:radial-gradient(ellipse at 60% 40%,#3a3a3a 0%,#262626 45%,#121212 100%)}
.hero-title{position:absolute;top:248px;width:1200px;text-align:center;font-family:var(--display);font-size:46px;line-height:70px;letter-spacing:4px}
.pill{position:absolute;background:var(--red);border-radius:32px;color:#fff;display:flex;align-items:center;justify-content:center;gap:10px;text-transform:uppercase}

/* sections */
.sec{position:absolute;left:0;width:1200px}
.welcome{top:844px;height:676px;background:linear-gradient(180deg,#181818,#1f1f1f)}
.about{top:1520px;height:676px;background:linear-gradient(90deg,#161616,#1d1d1d)}
.press{top:2196px;height:211px;background:var(--red)}
.packages{top:2407px;height:698px;background:#191919}
.stories{top:3105px;height:603px;background:linear-gradient(180deg,#1c1c1c,#151515)}
.contact{top:3708px;height:630px;background:linear-gradient(180deg,#1a1a1a,#222)}
.footer{top:4338px;height:368px;background:#0a0a0a}

.kicker{font-size:16px;font-weight:500;text-transform:uppercase}
.sec-title{font-family:var(--display);color:var(--red);text-transform:uppercase;letter-spacing:3px}
.para{font-size:13px;line-height:29px;color:#eee}

.feature{position:absolute;width:240px;text-align:center}
.feature svg{display:block;margin:0 auto}
.feature p{font-family:var(--display);font-size:14px;line-height:25px;letter-spacing:1.5px;margin-top:26px}

.portrait{position:absolute;left:151px;top:114px;width:428px;height:428px;border-radius:50%;background:radial-gradient(circle at 50% 40%,#d9d9d9,#8a8a8a 55%,#3a3a3a);border:6px solid #2a2a2a}

.press-box{position:absolute;top:51px;width:201px;height:109px;border:2px solid #fff;border-radius:4px;display:flex;align-items:center;justify-content:center;font-size:22px;font-weight:700;color:#fff;text-transform:uppercase}

.card{position:absolute;top:196px;width:306px;height:433px;background:var(--card);border-radius:4px;text-align:center}
.card .sale{margin-top:36px;font-size:19px;color:#fff;text-transform:uppercase}
.card .plan{margin-top:10px;font-family:var(--display);font-size:14px;letter-spacing:1.5px}
.card .price{margin-top:20px;color:var(--red);font-size:58px;font-weight:500;letter-spacing:1px}
.card .price sup{color:#fff;font-size:22px;vertical-align:30px}
.card .price small{color:#fff;font-size:12px}
.card .desc{font-size:13px;line-height:24px;color:#e6e6e6;padding:0 30px;margin-top:14px}
.card .desc + .desc{margin-top:16px}
.card .buy{position:absolute;left:78px;bottom:44px;width:150px;height:49px;background:var(--red);border-radius:25px;font-family:var(--display);font-size:15px;display:flex;align-items:center;justify-content:center}

.quote{position:absolute;width:270px;text-align:center}
.quote .mark{width:92px;height:92px;border:3px solid var(--red);border-radius:50%;margin:0 auto;display:flex;align-items:center;justify-content:center}
.quote p{font-size:13px;line-height:26px;margin-top:30px}
.quote .who{font-family:var(--display);color:var(--red);font-size:12px;margin-top:12px;letter-spacing:1.5px}
.quote .when{font-size:15px}

.field{position:absolute;left:345px;width:510px;border:1.5px solid #d8d8d8;padding:0 22px;font-size:14px;display:flex;align-items:center}

.info{position:absolute;top:30px;width:300px;text-align:center}
.info .ring{width:66px;height:66px;border:2px solid #fff;border-radius:50%;margin:0 auto;display:flex;align-items:center;justify-content:center}
.info h4{font-size:18px;font-weight:400;margin-top:24px;text-transform:uppercase}
.info p{font-size:11px;line-height:23px;color:#bbb;margin-top:6px}

.foot-nav{position:absolute;left:422px;top:249px;width:667px;display:flex;justify-content:space-between;font-size:12px;font-weight:500;text-transform:uppercase}
.social{position:absolute;top:300px;width:36px;height:36px;border:2px solid #fff;border-radius:50%}
</style>
</head>
<body>

<!-- header -->
<header>
  <div class="topbar"></div>
  <div class="navbar"></div>
  <a class="btn-outline" style="left:741px;width:227px">I need immediate services</a>
  <a class="btn-outline" style="left:981px;width:108px">Login</a>
  <nav class="main-nav">
    <span>Home</span><span>Falconry Institute</span><span>Testimonials</span><span>About</span><span>Upcoming Classes</span><span>Contact Us</span>
  </nav>
  <svg class="brand-shield" viewBox="0 0 216 219" aria-hidden="true">
    <path d="M0 0H216V175L108 219L0 175Z" fill="#000"/>
    <path d="M6 150V172L108 213L210 172V150" fill="none" stroke="#fff" stroke-width="2"/>
  </svg>
  <div class="brand-name" style="top:92px">Falconry<br>Institute</div>
</header>

<!-- hero -->
<section class="hero" role="img" aria-label="Dark photo of a pistol and loose cartridges on a textured surface">
  <h1 class="hero-title">Harbor Guard<br>Carry</h1>
  <a class="pill" style="left:321px;top:405px;width:170px;height:62px;font-size:14px;font-weight:500">Play now
    <svg width="16" height="16" viewBox="0 0 16 16"><circle cx="8" cy="8" r="6.5" fill="none" stroke="#fff" stroke-width="2"/><path d="M6.5 5L11 8L6.5 11Z" fill="#fff"/></svg>
  </a>
</section>

<!-- welcome -->
<section class="sec welcome">
  <div class="abs center display" style="top:80px;width:1200px;font-size:27px">Welcome to</div>
  <h2 class="abs center sec-title" style="top:122px;width:1200px;font-size:42px">Falconry Institute</h2>
  <p class="abs center para" style="left:222px;top:200px;width:756px">Wanna hear something funny? Guess what the average person asks about a concealed weapons class? "How much is it and how long is it?" Can you believe it? We are talking about preparing you for life and death situations and the main concern is "How Fast" and "How Cheap?" WOW!</p>

  <div class="feature" style="left:152px;top:340px">
    <svg width="186" height="186" viewBox="0 0 186 186" aria-hidden="true">
      <circle cx="93" cy="93" r="72" fill="none" stroke="var(--red)" stroke-width="9"/>
      <path d="M93 0V30M93 156V186M0 93H30M156 93H186" stroke="var(--red)" stroke-width="7"/>
      <g fill="none" stroke="#fff" stroke-width="2.5"><circle cx="93" cy="66" r="8"/><path d="M79 88Q93 76 107 88"/><circle cx="72" cy="98" r="7"/><circle cx="93" cy="98" r="7"/><circle cx="114" cy="98" r="7"/><path d="M60 120Q72 108 84 120M81 120Q93 108 105 120M102 120Q114 108 126 120"/></g>
    </svg>
    <p>Concealed<br>carry class</p>
  </div>
  <div class="feature" style="left:479px;top:340px">
    <svg width="186" height="186" viewBox="0 0 186 186" aria-hidden="true">
      <circle cx="93" cy="93" r="72" fill="none" stroke="var(--red)" stroke-width="9"/>
      <path d="M93 0V30M93 156V186M0 93H30M156 93H186" stroke="var(--red)" stroke-width="7"/>
      <g fill="none" stroke="#fff" stroke-width="3"><circle cx="93" cy="93" r="26"/><circle cx="93" cy="93" r="15"/><circle cx="93" cy="93" r="5" fill="#fff"/><path d="M93 58V70M93 116V128M58 93H70M116 93H128"/></g>
    </svg>
    <p>Dynamic<br>defensive shooting</p>
  </div>
  <div class="feature" style="left:815px;top:340px">
    <svg width="186" height="186" viewBox="0 0 186 186" aria-hidden="true">
      <circle cx="93" cy="93" r="72" fill="none" stroke="var(--red)" stroke-width="9"/>
      <path d="M93 0V30M93 156V186M0 93H30M156 93H186" stroke="var(--red)" stroke-width="7"/>
      <g fill="none" stroke="#fff" stroke-width="3" stroke-linecap="round"><path d="M70 70L116 116M116 70L70 116"/><circle cx="70" cy="70" r="7"/><rect x="108" y="108" width="14" height="14" transform="rotate(45 115 115)"/></g>
    </svg>
    <p>Fine tuning<br>your technique</p>
  </div>
</section>

<!-- about -->
<section class="sec about">
  <div class="portrait" role="img" aria-label="Black and white portrait photo of instructor Brendan Osterlow"></div>
  <div class="abs kicker" style="left:606px;top:63px">About the instructor</div>
  <h2 class="abs sec-title" style="left:606px;top:90px;font-size:36px;letter-spacing:2px">Brendan Osterlow</h2>
  <div class="abs para" style="left:606px;top:155px;width:483px;text-align:justify;line-height:25.7px">
    <p>Brendan Osterlow is a 3rd generation Jacksonville native and delighted to be a part of this great community. He is a true security expert with 25 years of experience in the security industry. He has appeared on Crest News, Channel Nine, Metro Seven &amp; Beacon News outlets. He has been Featured in numerous publications and has trained thousands to protect themselves and their homes from thugs and thieves. He is certified by both the NSL &amp; the NWDFA as a firearms instructor. He is also an NSL Range Safety Officer and Defensive Pistol Instructor. He often says: "My students are like family so I take their security personal. I want them to feel confident protect themselves their families!"</p>
    <p style="margin-top:25px">Harbor Guard Carry is a radically different concealed carry class focusing on the TRUTH about how "Real Attacks" take place. The Concealed Carry Class goes over way more than just the boring, lecture-style, gun shop curriculum into real strategies, tactics and training suggestions to help you prepare! You have to experience it to believe it!</p>
  </div>
</section>

<!-- press -->
<section class="sec press">
  <div class="press-box" style="left:150px">Channel Nine</div>
  <div class="press-box" style="left:384px">Metro Seven</div>
  <div class="press-box" style="left:619px">Crest News</div>
  <div class="press-box" style="left:853px">Beacon News</div>
</section>

<!-- packages -->
<section class="sec packages">
  <div class="abs center kicker" style="top:67px;width:1200px">Select your package</div>
  <h2 class="abs center sec-title" style="top:95px;width:1200px;font-size:36px">Falconry Institute</h2>

  <div class="card" style="left:111px">
    <div class="sale">Limited time sale</div>
    <div class="plan">Silver academy plan</div>
    <div class="price"><sup>$</sup>167<small>/mo</small></div>
    <p class="desc">Falconry Institute Level 2 Only "Master Combat Accuracy</p>
    <p class="desc">PLUS a discount if you upgrade to a package after</p>
    <a class="buy">Buy now</a>
  </div>
  <div class="card" style="left:447px">
    <div class="sale">Limited time sale</div>
    <div class="plan">Gold academy plan</div>
    <div class="price"><sup>$</sup>447<small>/mo</small></div>
    <p class="desc">Master Combat Accuracy, Live Fire Range &amp; Combat Simulator</p>
    <p class="desc">PLUS a discount if you upgrade to anytime before Level 4</p>
    <a class="buy">Buy now</a>
  </div>
  <div class="card" style="left:782px">
    <div class="sale">Limited time sale</div>
    <div class="plan">Platinum academy</div>
    <div class="price"><sup>$</sup>747<small>/mo</small></div>
    <p class="desc">Master Combat Accuracy, Live Fire Range, Combat Simulator</p>
    <p class="desc">Combat Pistol Live Fire, Empty Hand &amp; Force On Force"</p>
    <a class="buy">Buy now</a>
  </div>
</section>

<!-- stories -->
<section class="sec stories">
  <div class="abs center kicker" style="top:63px;width:1200px">Falconry Institute</div>
  <h2 class="abs center sec-title" style="top:94px;width:1200px;font-size:36px">Success stories</h2>

  <div class="quote" style="left:139px;top:204px">
    <div class="mark"><svg width="30" height="24" viewBox="0 0 30 24"><path d="M0 24V12Q0 2 10 0V5Q5 7 5 11H12V24ZM17 24V12Q17 2 27 0V5Q22 7 22 11H29V24Z" fill="#fff"/></svg></div>
    <p>"I had never held a gun when I took the Harbor Guard Carry class and I'm hooked! I'm going all the way to Thank you Harbor Guard Carry!</p>
    <div class="who">Marla K.</div>
    <div class="when">October 14, 2017</div>
  </div>
  <div class="quote" style="left:464px;top:204px">
    <div class="mark"><svg width="30" height="24" viewBox="0 0 30 24"><path d="M0 24V12Q0 2 10 0V5Q5 7 5 11H12V24ZM17 24V12Q17 2 27 0V5Q22 7 22 11H29V24Z" fill="#fff"/></svg></div>
    <p>"I was mugged here in Jacksonville and lived in fear ever since. It stole my happiness and I became scared to go out. I'm a Level 4 student and I feel sorry for the next thug that tries me!"</p>
    <div class="who">Denise R.</div>
    <div class="when">December 9, 2017</div>
  </div>
  <div class="quote" style="left:795px;top:204px">
    <div class="mark"><svg width="30" height="24" viewBox="0 0 30 24"><path d="M0 24V12Q0 2 10 0V5Q5 7 5 11H12V24ZM17 24V12Q17 2 27 0V5Q22 7 22 11H29V24Z" fill="#fff"/></svg></div>
    <p>I've been shooting for years and already had my concealed weapons license. My first class was a gun shop class and a waste of money. Brendan took the time to show me how to properly grip</p>
    <div class="who">Frank H.</div>
    <div class="when">March 3 2018</div>
  </div>
</section>

<!-- contact -->
<section class="sec contact">
  <div class="abs center kicker" style="top:56px;width:1200px">Falconry Institute</div>
  <h2 class="abs center sec-title" style="top:86px;width:1200px;font-size:36px">Get in touch</h2>
  <div class="field" style="top:168px;height:55px">Name :</div>
  <div class="field" style="top:239px;height:55px">Email :</div>
  <div class="field" style="top:309px;height:54px">Phone :</div>
  <div class="field" style="top:380px;height:117px;align-items:flex-start;padding-top:18px">Message :</div>
  <a class="pill" style="left:515px;top:524px;width:170px;height:53px;font-family:var(--display);font-size:16px">Send</a>
</section>

<!-- footer -->
<footer class="sec footer">
  <div class="info" style="left:118px">
    <div class="ring"><svg width="20" height="26" viewBox="0 0 20 26"><path d="M10 25Q0 13 0 10A10 10 0 0 1 20 10Q20 13 10 25Z" fill="#fff"/><circle cx="10" cy="10" r="3.5" fill="#0a0a0a"/></svg></div>
    <h4>Location</h4>
    <p>P.O. Box 4172<br>Cedar Point, FL 32099</p>
  </div>
  <div class="info" style="left:451px">
    <div class="ring"><svg width="22" height="22" viewBox="0 0 24 24"><path d="M6.6 10.8a15.2 15.2 0 0 0 6.6 6.6l2.2-2.2a1 1 0 0 1 1-.25 11.4 11.4 0 0 0 3.6.57 1 1 0 0 1 1 1V20a1 1 0 0 1-1 1A17 17 0 0 1 3 4a1 1 0 0 1 1-1h3.5a1 1 0 0 1 1 1c0 1.25.2 2.45.57 3.6a1 1 0 0 1-.25 1Z" fill="#fff"/></svg></div>
    <h4>Contact</h4>
    <p>Office: 904-555-0148<br>Toll-free: 844-555-0192</p>
  </div>
  <div class="info" style="left:781px">
    <div class="ring"><svg width="24" height="18" viewBox="0 0 24 18"><rect width="24" height="18" rx="2" fill="#fff"/><path d="M1 2L12 10L23 2" fill="none" stroke="#0a0a0a" stroke-width="2"/></svg></div>
    <h4>Email</h4>
    <p>hello@harborguardcarry.example</p>
  </div>

  <div class="abs" style="left:108px;top:214px;width:981px;height:1px;background:#2c2c2c"></div>
  <div class="abs" style="left:141px;top:252px;width:160px;text-align:center;font-family:var(--display);font-size:18px;line-height:24px;text-transform:uppercase">Falconry<br>Institute</div>
  <nav class="foot-nav">
    <span>Home</span><span>Falconry Institute</span><span>Testimonials</span><span>About</span><span>Upcoming Classes</span><span>Contact Us</span>
  </nav>
  <div class="abs" style="left:422px;top:310px;font-size:13px">©2021 Falconry Institute . All rights reserved.</div>
  <span class="social" style="left:965px" aria-label="Social profile one"></span>
  <span class="social" style="left:1008px" aria-label="Social profile two"></span>
  <span class="social" style="left:1052px" aria-label="Social profile three"></span>
</footer>

</body>
</html>
```